Business Card for Bloom Vitality & Strength

Hi can you please design a business card with my logo and program logo (the new one I just sent) somewhere on it too maybe on the back? Needs to be eye catching and super cool.
Trudy Melcombe, Director
Master Personal Trainer & Nutrition Coach
0472 816 305
Www.bloomvitalitystrength.com.au
Insta (logo) bloom_vitality_strength #bloomyou7x72018

Target Market(s)

30+ women looking to change lifestyle to healthy mind body etc

Industry/Entity Type

Health And Wellness

Contact Information for Business Card

As above

Font styles to use
Sans Serif

Colors

Designer to choose colors to be used in the design.

Requirements
Must have
• Must super cool and edgy with a bit of cuteness

```html
<!DOCTYPE html>
<html lang="en">
<head>
<meta charset="utf-8">
<title>Bloom Vitality &amp; Strength — Business Card</title>
<link rel="stylesheet" href="https://fonts.googleapis.com/css2?family=Open+Sans:wght@400;600;700&display=swap">
<style>
  :root {
    --backdrop: #ece9e5;
    --card-white: #ffffff;
    --brand-red: #d11a1a;
    --brand-red-bright: #e01f1f;
    --brand-red-deep: #a31b1b;
    --ink: #1d1d1d;
    --ink-soft: #4a4a4a;
    --rule: #555555;
  }
  * { box-sizing: border-box; margin: 0; padding: 0; }
  html, body {
    width: 1200px; height: 1000px; overflow: hidden;
    background: var(--backdrop);
    font-family: "Open Sans", Arial, sans-serif;
  }
  .stage { position: relative; width: 1200px; height: 1000px; }

  .card {
    position: absolute; top: 252px;
    width: 495px; height: 495px;
    box-shadow: 0 4px 14px rgba(0,0,0,0.18);
  }

  /* Front */
  .card-front {
    left: 73px;
    background: radial-gradient(circle at 50% 48%, var(--brand-red-bright) 0%, var(--brand-red) 40%, var(--brand-red-deep) 100%);
    display: flex; align-items: center; justify-content: center;
  }
  .front-wordmark {
    color: var(--card-white);
    font-weight: 700;
    text-align: center;
    line-height: 1.15;
  }
  .front-wordmark .line-main { display: block; font-size: 38px; letter-spacing: 0.5px; }
  .front-wordmark .line-sub { display: block; font-size: 22px; letter-spacing: 9px; margin-top: 6px; }

  /* Back */
  .card-back {
    left: 627px;
    background: var(--card-white);
    text-align: center;
    color: var(--ink);
  }
  .program-mark {
    position: absolute; top: 72px; left: 0; right: 0;
    display: flex; align-items: center; justify-content: center; gap: 10px;
    color: var(--ink-soft); font-weight: 400;
  }
  .program-mark .dot {
    width: 14px; height: 14px; border-radius: 50%;
    background: var(--brand-red);
  }
  .program-mark .program-name { font-size: 28px; letter-spacing: 2px; }
  .program-by {
    position: absolute; top: 130px; left: 0; right: 0;
    font-size: 10px; color: var(--ink-soft); padding-left: 120px;
  }

  .person { position: absolute; top: 198px; left: 0; right: 0; }
  .person-name { font-size: 19px; font-weight: 700; color: var(--brand-red); letter-spacing: 0.3px; }
  .person-role { font-size: 15.5px; line-height: 1.3; }
  .person-title { font-size: 15.5px; margin-top: 6px; }

  .divider {
    position: absolute; top: 281px; left: 226px;
    width: 44px; height: 1px; background: var(--rule);
  }

  .contact-icons {
    position: absolute; top: 299px; left: 0; right: 0;
    display: flex; justify-content: center; gap: 8px;
  }
  .contact-icons svg { width: 14px; height: 12px; fill: var(--brand-red); }

  .contact { position: absolute; top: 320px; left: 0; right: 0; font-size: 16px; line-height: 24px; }

  .social-marker {
    position: absolute; top: 384px; left: 240px;
    width: 15px; height: 15px; border-radius: 50%;
    border: 2px solid var(--brand-red);
  }
  .social { position: absolute; top: 401px; left: 0; right: 0; font-size: 16px; line-height: 25px; }
</style>
</head>
<body>
<main class="stage">

  <section class="card card-front" aria-label="Card front">
    <h1 class="front-wordmark">
      <span class="line-main">BLOOM VITALITY</span>
      <span class="line-sub">&amp; STRENGTH</span>
    </h1>
  </section>

  <section class="card card-back" aria-label="Card back">
    <div class="program-mark">
      <span class="dot"></span>
      <span class="program-name">BloomYou7x7 fitMETHOD</span>
    </div>
    <div class="program-by">By Bloom Vitality &amp; Strength</div>

    <div class="person">
      <h2 class="person-name">TRUDY MELCOMBE</h2>
      <p class="person-role">- Director -</p>
      <p class="person-title">Master Personal Trainer &amp; Nutrition Coach</p>
    </div>

    <div class="divider"></div>

    <div class="contact-icons">
      <svg viewBox="0 0 14 12" aria-label="Phone"><path d="M2 3 Q7 0 12 3 L11 5 L9 4.5 L9 3.5 Q7 3 5 3.5 L5 4.5 L3 5 Z M4 6 H10 L11.5 11 H2.5 Z"/></svg>
      <svg viewBox="0 0 14 12" aria-label="Email"><path d="M1 1.5 H13 V10.5 H1 Z M1.8 2.3 L7 6.5 L12.2 2.3" stroke="#fff" stroke-width="1"/></svg>
    </div>

    <div class="contact">
      <p>0472 816 305</p>
      <p>www.bloomvitalitystrength.com.au</p>
    </div>

    <span class="social-marker"></span>
    <div class="social">
      <p>bloom_vitality_strength</p>
      <p>#bloomyou7x72018</p>
    </div>
  </section>

</main>
</body>
</html>
```